DeskHarbour Flyer

I require an A5 sized flyer to be designed that advertised the new flexible workspace of DeskHarbour.
should say it is a "Flexible Workspace with EV Charging"
web address is www.deskharbour-example.co.uk
It should show the 3 different types of membership as priced on the website

```html
<!DOCTYPE html>
<html lang="en">
<head>
<meta charset="utf-8">
<title>DeskHarbour Flyer</title>
<link rel="stylesheet" href="https://fonts.googleapis.com/css2?family=Poppins:ital,wght@0,300;0,400;0,500;0,600;0,700;0,800;0,900;1,700;1,800;1,900&display=swap">
<style>
:root{
  --orange:#e0820f;
  --blue:#3f6fe0;
  --charcoal:#3b3b3b;
  --ink:#2e2e2e;
  --paper:#ffffff;
  --card-body:#efefef;
  --backdrop:#d9d9d9;
}
*{box-sizing:border-box;margin:0;padding:0}
html,body{width:1200px;height:2395px;overflow:hidden;background:var(--backdrop);font-family:'Poppins',sans-serif;color:var(--ink)}
.flyer{position:absolute;left:40px;top:404px;width:961px;height:1362px;background:var(--paper);transform:scale(1.1655);transform-origin:0 0;box-shadow:0 10px 30px rgba(0,0,0,.18);overflow:hidden}
.abs{position:absolute}
.brand{left:55px;top:60px;font-weight:800;font-size:48px;letter-spacing:-1px;color:var(--ink)}
.headline{left:56px;top:150px;font-style:italic;font-weight:900;line-height:1}
.headline .l1{font-size:66px;color:var(--ink);display:block}
.headline .l2{font-size:42px;color:var(--ink);display:block;margin-top:6px}
.headline .l2 .thin{font-weight:400;font-style:normal}
.headline .l3{font-size:57px;color:var(--orange);display:block;margin-top:6px;margin-left:-5px}
.rule{left:58px;top:340px;width:397px;height:2px;background:#9a9a9a}
.charger-car{left:15px;top:365px;width:455px;height:355px;border-radius:6px;background:linear-gradient(135deg,#f4f4f4 0%,#dfe3ea 45%,#b9c7de 75%,#f5f6f8 100%)}
.tagline{left:170px;top:376px;font-style:italic;font-weight:800;font-size:20px;line-height:24px;color:var(--ink)}
.tagline .accent{color:var(--orange)}
.photo-frame{left:485px;top:45px;width:476px;height:407px;border-top:13px solid var(--orange);border-left:12px solid var(--orange);border-bottom-left-radius:110px;clip-path:polygon(0 0,55.5% 0,55.5% 6%,100% 6%,100% 100%,0 100%)}
.photo{left:508px;top:70px;width:453px;height:382px;border-bottom-left-radius:95px;background:linear-gradient(180deg,#e9ecef 0%,#d4d9de 40%,#9a9da0 70%,#6f6d6a 100%)}
.section-title{left:498px;top:472px;font-weight:600;font-size:27px;color:var(--ink)}
.section-title span{color:var(--orange)}
.intro{left:501px;top:519px;width:410px;font-size:15.5px;line-height:19.5px}
.intro.strong{top:610px;width:420px}
.intro.strong b{color:var(--orange);font-weight:700}
.card{top:760px;width:264px;height:475px;border:4px solid;border-radius:12px;background:var(--paper);padding:5px}
.card-inner{position:relative;width:100%;height:100%;background:var(--card-body);border-radius:4px;overflow:hidden}
.card-tab{top:727px;width:104px;height:38px;border-radius:8px 8px 0 0;display:flex;align-items:center;justify-content:center}
.card-head{position:absolute;left:0;top:0;width:100%;height:92px;clip-path:polygon(0 0,100% 0,100% 45%,50% 100%,0 45%);color:#fff;text-align:center;font-weight:700;font-size:19px;line-height:21px;padding-top:6px}
.card-shade{position:absolute;left:0;top:0;width:100%;height:112px;background:linear-gradient(180deg,#d9d9d9,#efefef);clip-path:polygon(0 0,100% 0,100% 55%,50% 100%,0 55%)}
.features{position:absolute;left:24px;top:100px;right:14px;list-style:none;font-size:14.5px;line-height:18px}
.features li{position:relative;padding-left:20px;margin-bottom:2px}
.features li svg{position:absolute;left:0;top:4px;width:11px;height:11px}
.all .features{font-size:13.5px;line-height:16.5px;top:96px;left:18px;right:10px}
.all .features li{margin-bottom:3px}
.price{position:absolute;left:50%;transform:translateX(-50%);top:378px;width:152px;height:42px;border-radius:9px;color:#fff;font-weight:700;font-size:14px;line-height:15px;display:flex;align-items:center;justify-content:center;text-align:center}
.price-note{position:absolute;left:0;right:0;top:428px;text-align:center;font-size:10.5px}
.day{left:85px;border-color:var(--orange)}
.light{left:350px;border-color:var(--blue)}
.all{left:614px;border-color:var(--charcoal)}
.day .card-head,.day .price,.tab-day{background:var(--orange)}
.light .card-head,.light .price,.tab-light{background:var(--blue)}
.all .card-head,.all .price,.tab-all{background:var(--charcoal)}
.tab-day{left:165px}.tab-light{left:429px}.tab-all{left:693px}
.day li svg{color:var(--orange)}.light li svg{color:var(--blue)}.all li svg{color:#666}
.contact{left:57px;top:1263px;width:846px;height:43px;border-radius:22px;background:var(--charcoal);display:flex;align-items:center;color:#fff;font-size:16px;overflow:hidden;white-space:nowrap}
.contact .label{flex-shrink:0;background:var(--orange);height:100%;padding:0 14px;display:flex;align-items:center;font-weight:700;font-size:18px;border-radius:22px 0 0 22px}
.contact .item{flex-shrink:0;display:flex;align-items:center;gap:8px;padding:0 16px}
.contact .sep{flex-shrink:0;width:1px;height:26px;background:#999}
.contact svg{width:17px;height:17px;color:var(--orange);flex-shrink:0}
</style>
</head>
<body>
<main class="flyer">
  <div class="abs brand">DeskHarbour</div>

  <h1 class="abs headline">
    <span class="l1">FLEXIBLE</span>
    <span class="l2">WORKSPACE <span class="thin">WITH</span></span>
    <span class="l3">EV CHARGING</span>
  </h1>
  <div class="abs rule"></div>

  <div class="abs charger-car" role="img" aria-label="EV charging post plugged into a silver electric car"></div>
  <p class="abs tagline">CHARGE YOUR EV,<br>GET SOME<br><span class="accent">WORKSPACE<br>AND REFUEL!</span></p>

  <div class="abs photo-frame"></div>
  <div class="abs photo" role="img" aria-label="Open-plan workspace interior with kitchen, bar seating and lounge chairs"></div>

  <h2 class="abs section-title">EV Charging <span>and Workspace</span></h2>
  <p class="abs intro">DeskHarbour is a unique workspace environment for EV owners looking to recharge their Electric Vehicles, grab a snack and beverage, and catch up with some office work</p>
  <p class="abs intro strong"><b>Flexible memberships are available for regular users</b> of the workspace which include preferential discounts to EV charging rates</p>

  <svg width="0" height="0" style="position:absolute">
    <symbol id="tick" viewBox="0 0 12 12"><circle cx="6" cy="6" r="5" fill="none" stroke="currentColor" stroke-width="1.2"/><path d="M3.5 6.2l1.7 1.7 3.3-3.4" fill="none" stroke="currentColor" stroke-width="1.3"/></symbol>
  </svg>

  <div class="abs card-tab tab-day"><svg width="24" height="20" viewBox="0 0 24 20" fill="none" stroke="#fff" stroke-width="1.8"><rect x="2" y="5" width="20" height="13" rx="2"/><path d="M8 5V2h8v3M2 10h20"/></svg></div>
  <div class="abs card-tab tab-light"><svg width="24" height="24" viewBox="0 0 24 24" fill="none" stroke="#fff" stroke-width="1.8"><circle cx="11" cy="13" r="8"/><circle cx="11" cy="13" r="4"/><path d="M11 13l9-9M17 4h3v3"/></svg></div>
  <div class="abs card-tab tab-all"><svg width="24" height="22" viewBox="0 0 24 22" fill="none" stroke="#fff" stroke-width="1.6"><path d="M6 3h12l4 5-10 12L2 8z M2 8h20 M9 3l3 17 3-17"/></svg></div>

  <section class="abs card day"><div class="card-inner">
    <div class="card-shade"></div>
    <div class="card-head">Day<br>Member</div>
    <ul class="features">
      <li><svg><use href="#tick"/></svg>Use of Hot Desks &amp; Lounge Areas</li>
      <li><svg><use href="#tick"/></svg>Secure Wifi</li>
      <li><svg><use href="#tick"/></svg>Free Tea &amp; Coffee</li>
    </ul>
    <div class="price">£25.00<br>EACH VISIT</div>
    <div class="price-note">Price Inclusive of VAT Per month</div>
  </div></section>

  <section class="abs card light"><div class="card-inner">
    <div class="card-shade"></div>
    <div class="card-head">Light<br>Member</div>
    <ul class="features">
      <li><svg><use href="#tick"/></svg>Use of Hot Desks &amp; Lounge Areas</li>
      <li><svg><use href="#tick"/></svg>Secure Wifi</li>
      <li><svg><use href="#tick"/></svg>Free Tea &amp; Coffee Discounted E/V Charge Rates</li>
      <li><svg><use href="#tick"/></svg>Access to Meeting Rooms (£10+vat per person, per hour)</li>
    </ul>
    <div class="price">£18 A MONTH +<br>£18 EACH VISIT</div>
    <div class="price-note">Price Inclusive of VAT Per month</div>
  </div></section>

  <section class="abs card all"><div class="card-inner">
    <div class="card-shade"></div>
    <div class="card-head">All Access<br>Member</div>
    <ul class="features">
      <li><svg><use href="#tick"/></svg>Unlimited Number of Visits Each Month</li>
      <li><svg><use href="#tick"/></svg>Dedicated Desk</li>
      <li><svg><use href="#tick"/></svg>(lockable draws + £60 a month)</li>
      <li><svg><use href="#tick"/></svg>Receptionist to Meet &amp; Greet Guests</li>
      <li><svg><use href="#tick"/></svg>Use of Lounge Areas</li>
      <li><svg><use href="#tick"/></svg>Secure Wifi</li>
      <li><svg><use href="#tick"/></svg>Free Tea &amp; Coffee</li>
      <li><svg><use href="#tick"/></svg>Discounted E/V Charge Rates</li>
      <li><svg><use href="#tick"/></svg>Access to Meeting Rooms (£10+vat per person, per h)</li>
    </ul>
    <div class="price">£180.00</div>
    <div class="price-note">Price Inclusive of VAT Per month</div>
  </div></section>

  <footer class="abs contact">
    <span class="label">CONTACT US</span>
    <span class="item"><svg viewBox="0 0 20 20" fill="none" stroke="currentColor" stroke-width="2"><rect x="2" y="4" width="16" height="12"/><path d="M2 4l8 7 8-7"/></svg>info@deskharbour-example.co.uk</span>
    <span class="sep"></span>
    <span class="item"><svg viewBox="0 0 20 20" fill="none" stroke="currentColor" stroke-width="1.8"><circle cx="10" cy="10" r="8"/><path d="M2 10h16M10 2c3 3 3 13 0 16M10 2c-3 3-3 13 0 16"/></svg>www.deskharbour-example.co.uk</span>
  </footer>
</main>
</body>
</html>
```